Healthcare Consulting company business card

We are looking for a business card design for a new healthcare consulting company. The company is looking to provide assistance to large healthcare organisations in the following categories:
Acute care and critical care
Tender documents and applications
CV, job applications and interview skills
scientific lecture presentation preparations and skills
research and quality activities
medical equipment and device consulting
hemofiltration liaising.
Please see the attached file below for the design brief.
Alternative designs are welcomed.
Business
Contact Information for Business Card
Name: Rex Tulloch
Mobile: 0427 816 094
Email: rextullochconsulting@mailbox-example.com
Website: www.rextullochconsulting-example.com.au

```html
<!DOCTYPE html>
<html lang="en">
<head>
<meta charset="utf-8">
<title>Rex Tulloch Consulting – Business Card</title>
<link rel="stylesheet" href="https://fonts.googleapis.com/css2?family=Arimo:wght@400;700&display=swap">
<style>
  :root {
    --brand-blue: #1656a6;
    --card-white: #ffffff;
    --backdrop: #e9e6e1;
    --text-blue: #1656a6;
  }
  * { box-sizing: border-box; margin: 0; padding: 0; }
  html, body { width: 1200px; height: 800px; overflow: hidden; }
  body {
    background: var(--backdrop);
    font-family: "Arimo", Arial, sans-serif;
    display: flex;
    align-items: center;
    justify-content: center;
    gap: 60px;
  }
  .icon-defs { position: absolute; width: 0; height: 0; }
  .card {
    position: relative;
    width: 520px;
    height: 298px;
    border-radius: 12px;
    box-shadow: 0 6px 18px rgba(0,0,0,0.12);
    overflow: hidden;
  }
  .card--front { background: var(--brand-blue); color: var(--card-white); }
  .card--back { background: var(--card-white); color: var(--text-blue); }

  .wordmark { text-align: center; font-weight: 700; line-height: 1; }
  .wordmark__name { display: block; letter-spacing: 0.02em; }
  .wordmark__tag { display: block; letter-spacing: 0.32em; }

  .card--front .wordmark { position: absolute; top: 62px; left: 0; right: 0; }
  .card--front .wordmark__name { font-size: 38px; }
  .card--front .wordmark__tag { font-size: 19px; margin-top: 6px; }

  .service-row { position: absolute; display: flex; list-style: none; justify-content: space-between; }
  .card--front .service-row { left: 40px; right: 40px; bottom: 34px; }
  .card--back .service-row { left: 32px; right: 52px; bottom: 28px; }

  .service-icon {
    width: 50px; height: 50px;
    border-radius: 2px;
    display: flex; align-items: center; justify-content: center;
  }
  .service-icon svg { width: 40px; height: 40px; }
  .card--front .service-icon { background: var(--card-white); color: var(--brand-blue); }
  .card--back .service-icon { background: var(--brand-blue); color: var(--card-white); }

  .contact {
    position: absolute;
    top: 30px; left: 32px;
    font-size: 16.5px;
    line-height: 1.2;
  }
  .contact__name { font-size: 19px; text-transform: uppercase; letter-spacing: 0.02em; }

  .card--back .wordmark { position: absolute; right: 26px; top: 132px; }
  .card--back .wordmark__name { font-size: 22px; }
  .card--back .wordmark__tag { font-size: 12px; margin-top: 4px; }
</style>
</head>
<body>
  <svg class="icon-defs" aria-hidden="true">
    <defs>
      <symbol id="icon-tender" viewBox="0 0 24 24" fill="none" stroke="currentColor" stroke-width="1.6" stroke-linejoin="round" stroke-linecap="round">
        <path d="M6 3h9l4 4v14H6z"/><path d="M15 3v4h4"/>
        <circle cx="12.5" cy="14" r="4"/><path d="M12.5 11.5v5M13.8 12.5h-2a0.9 0.9 0 0 0 0 1.6h1.4a0.9 0.9 0 0 1 0 1.6h-2"/>
      </symbol>
      <symbol id="icon-heart" viewBox="0 0 24 24" fill="none" stroke="currentColor" stroke-width="1.6" stroke-linejoin="round" stroke-linecap="round">
        <path d="M12 20.5 4 12.8A4.6 4.6 0 0 1 12 7a4.6 4.6 0 0 1 8 5.8z"/>
        <path d="M2 12h5l1.5-3 2.5 6 2-4.5 1.2 1.5H22"/>
      </symbol>
      <symbol id="icon-bed" viewBox="0 0 24 24" fill="none" stroke="currentColor" stroke-width="1.6" stroke-linejoin="round" stroke-linecap="round">
        <path d="M3 8v12M3 16h18v4M21 16v-3a2 2 0 0 0-2-2H10v5"/>
        <circle cx="6.5" cy="13" r="1.6"/>
        <rect x="13" y="3" width="8" height="5" rx="0.5"/><path d="M14.5 5.5h1l.8-1.2 1 2.2.7-1h1.5"/>
      </symbol>
      <symbol id="icon-filter" viewBox="0 0 24 24" fill="none" stroke="currentColor" stroke-width="1.6" stroke-linejoin="round" stroke-linecap="round">
        <path d="M12 3s-5 6-5 9.5a5 5 0 0 0 10 0C17 9 12 3 12 3z"/>
        <path d="M4 20h16M9.5 13.5a2.5 2.5 0 0 0 2.5 2.5"/>
      </symbol>
      <symbol id="icon-lab" viewBox="0 0 24 24" fill="none" stroke="currentColor" stroke-width="1.6" stroke-linejoin="round" stroke-linecap="round">
        <path d="M4 6v12a2 2 0 0 0 4 0V6M3 6h6M4 12h4"/>
        <path d="M13 21h8M15 18h4M16 4l3 2-4 6-3-2zM18 10a4 4 0 0 1-1.5 8"/>
      </symbol>
    </defs>
  </svg>

  <section class="card card--front" aria-label="Card front">
    <div class="wordmark">
      <span class="wordmark__name">REX TULLOCH</span>
      <span class="wordmark__tag">CONSULTING</span>
    </div>
    <ul class="service-row">
      <li class="service-icon" role="img" aria-label="Tenders and applications"><svg><use href="#icon-tender"/></svg></li>
      <li class="service-icon" role="img" aria-label="Acute and critical care"><svg><use href="#icon-heart"/></svg></li>
      <li class="service-icon" role="img" aria-label="Hospital equipment"><svg><use href="#icon-bed"/></svg></li>
      <li class="service-icon" role="img" aria-label="Hemofiltration liaising"><svg><use href="#icon-filter"/></svg></li>
      <li class="service-icon" role="img" aria-label="Research and quality"><svg><use href="#icon-lab"/></svg></li>
    </ul>
  </section>

  <section class="card card--back" aria-label="Card back">
    <div class="contact">
      <p class="contact__name">Rex Tulloch</p>
      <p class="contact__phone">0427 816 094</p>
      <p class="contact__email">rextullochconsulting@mailbox-example.com</p>
      <p class="contact__web">www.rextullochconsulting-example.com.au</p>
    </div>
    <div class="wordmark">
      <span class="wordmark__name">REX TULLOCH</span>
      <span class="wordmark__tag">CONSULTING</span>
    </div>
    <ul class="service-row">
      <li class="service-icon" role="img" aria-label="Tenders and applications"><svg><use href="#icon-tender"/></svg></li>
      <li class="service-icon" role="img" aria-label="Acute and critical care"><svg><use href="#icon-heart"/></svg></li>
      <li class="service-icon" role="img" aria-label="Hospital equipment"><svg><use href="#icon-bed"/></svg></li>
      <li class="service-icon" role="img" aria-label="Hemofiltration liaising"><svg><use href="#icon-filter"/></svg></li>
      <li class="service-icon" role="img" aria-label="Research and quality"><svg><use href="#icon-lab"/></svg></li>
    </ul>
  </section>
</body>
</html>
```